Halvorn spray foam and Environmental

I have business cards but need new ones. The ones I have are very bland. Here is. Y company website http://www.halvornsprayfoam.ca

Also I can send you copies of the current cards
I would also need my current logo on the new design as well.. Also spray foam and Environmental

Industry/Entity Type

Business

Logo Text

Halvorn.

```html
<!DOCTYPE html>
<html lang="en">
<head>
<meta charset="utf-8">
<title>Halvorn Spray Foam Ltd. — Business Card</title>
<link href="https://fonts.googleapis.com/css2?family=Work+Sans:wght@400;500;600;700&family=Crimson+Text&display=swap" rel="stylesheet">
<style>
  :root{
    --bg:#1a1a1b;
    --card:#262627;
    --card-edge:#2f2f30;
    --purple:#7b3fa0;
    --grey-text:#8a8a8a;
    --mark:#6d6d70;
    --white:#f2f2f2;
  }
  *{margin:0;padding:0;box-sizing:border-box}
  html,body{width:1200px;height:900px;overflow:hidden;background:var(--bg)}
  .stage{position:relative;width:1200px;height:900px}
  .card{
    position:absolute;left:260px;width:680px;height:388px;
    background:linear-gradient(135deg,var(--card-edge),var(--card) 60%);
    box-shadow:0 14px 30px rgba(0,0,0,.55);
  }
  .card--front{top:48px}
  .card--back{top:466px}
  .brand{display:flex;align-items:center;gap:14px}
  .brand__mark{width:54px;height:40px;border-radius:6px;background:var(--mark)}
  .brand__name{
    font-family:"Work Sans",sans-serif;font-weight:700;color:var(--purple);
    font-size:30px;letter-spacing:.5px;line-height:1;text-transform:uppercase;
  }
  .brand__sub{
    font-family:"Work Sans",sans-serif;font-weight:700;color:var(--purple);
    font-size:15px;letter-spacing:.5px;margin-top:6px;text-transform:uppercase;
  }
  .tagline{
    font-family:"Crimson Text",serif;color:var(--grey-text);font-size:30px;
    line-height:1;margin-top:10px;
  }
  .card--front .brand-block{position:absolute;left:175px;top:118px}
  .card--front .url{
    position:absolute;left:0;right:0;top:322px;text-align:center;
    font-family:"Work Sans",sans-serif;color:var(--white);font-size:15px;letter-spacing:1.5px;
  }
  .card--back .brand-block{position:absolute;left:40px;top:130px}
  .card--back .brand__name{font-size:26px}
  .card--back .brand__sub{font-size:13px}
  .card--back .tagline{font-size:26px}
  .divider{position:absolute;left:375px;top:98px;width:2px;height:196px;background:var(--purple)}
  .contact{position:absolute;left:405px;top:98px;font-family:"Work Sans",sans-serif;color:var(--white)}
  .contact__name{color:var(--purple);font-size:26px;font-weight:500;letter-spacing:3px;text-transform:uppercase}
  .contact__role{font-size:16px;letter-spacing:1px;margin-top:2px}
  .contact__addr{font-size:16px;letter-spacing:1px;line-height:1.3;margin-top:14px}
  .contact__list{list-style:none;margin-top:10px}
  .contact__list li{display:flex;align-items:center;gap:10px;font-size:16px;letter-spacing:1px;line-height:1.4}
  .contact__list svg{width:11px;height:11px;flex:none}
</style>
</head>
<body>
<main class="stage">
  <section class="card card--front">
    <div class="brand-block">
      <div class="brand">
        <span class="brand__mark"></span>
        <div>
          <div class="brand__name">Halvorn</div>
          <div class="brand__sub">Spray Foam Ltd.</div>
        </div>
      </div>
      <div class="tagline">Residential &amp; Commercial</div>
    </div>
    <div class="url">www.halvornsprayfoam.ca</div>
  </section>

  <section class="card card--back">
    <div class="brand-block">
      <div class="brand">
        <span class="brand__mark"></span>
        <div>
          <div class="brand__name">Halvorn</div>
          <div class="brand__sub">Spray Foam Ltd.</div>
        </div>
      </div>
      <div class="tagline">Residential &amp; Commercial</div>
    </div>
    <div class="divider"></div>
    <div class="contact">
      <div class="contact__name">Dorian Vale</div>
      <div class="contact__role">Founder</div>
      <div class="contact__addr">4820 Larchmont Way Burnaby,<br>British Columbia v5h 2k9, CA</div>
      <ul class="contact__list">
        <li><svg viewBox="0 0 12 12"><path d="M2 1h3l1 3-2 1a7 7 0 0 0 3 3l1-2 3 1v3a1 1 0 0 1-1 1A10 10 0 0 1 1 2a1 1 0 0 1 1-1z" fill="none" stroke="#7b3fa0" stroke-width="1.2"/></svg>(604) 555-0192</li>
        <li><svg viewBox="0 0 12 12"><rect x="1" y="2.5" width="10" height="7" fill="none" stroke="#7b3fa0" stroke-width="1.2"/><path d="M1 2.5l5 4 5-4" fill="none" stroke="#7b3fa0" stroke-width="1.2"/></svg>halvornfoam@mailbox.ca</li>
        <li><svg viewBox="0 0 12 12"><circle cx="6" cy="6" r="5" fill="none" stroke="#7b3fa0" stroke-width="1.2"/><ellipse cx="6" cy="6" rx="2" ry="5" fill="none" stroke="#7b3fa0" stroke-width="1"/><path d="M1 6h10" stroke="#7b3fa0" stroke-width="1"/></svg>www.halvornsprayfoam.ca</li>
      </ul>
    </div>
  </section>
</main>
</body>
</html>
```